Business cards for Harbourline Supply Pty Ltd that import building products into Australia from China
Target Market(s)
Business to Business
Industry/Entity Type
Business
Contact Information for Business Card
Front: Logo and Business Name
Rear:
Vernon Ashcombe
General Manager
Mobile: 0427 619 354
email: vern@harbourlinesupply.com.au
alternative email: vern@coastwardgoods.com.au
web: www.harbourlinesupply.com.au
Adelaide, Brisbane and Darwin
Colors
ec1f27
fbee3d

```html
<!DOCTYPE html>
<html lang="en">
<head>
<meta charset="utf-8">
<title>Harbourline Supply Pty Ltd – Business Cards</title>
<link href="https://fonts.googleapis.com/css2?family=Open+Sans:wght@400;600;700&display=swap" rel="stylesheet">
<style>
  :root {
    --page: #e9e7e3;
    --card-dark: #2e2e30;
    --card-light: #ffffff;
    --brand-red: #ec1f27;
    --ink: #1c1c1c;
    --ink-soft: #3a3a3a;
    --logo-grey: #6c6c6e;
  }
  * { margin: 0; padding: 0; box-sizing: border-box; }
  html, body {
    width: 1200px; height: 800px; overflow: hidden;
    background: var(--page);
    font-family: "Open Sans", Arial, sans-serif;
  }
  .canvas {
    position: relative; width: 1200px; height: 800px;
  }
  .card {
    position: absolute; top: 242px;
    width: 520px; height: 316px;
    border-radius: 18px; overflow: hidden;
    box-shadow: 0 6px 18px rgba(0,0,0,.18);
  }
  .card--front { left: 50px; background: var(--card-dark); }
  .card--back { left: 630px; background: var(--card-light); }

  /* front */
  .front-brand {
    position: absolute; left: 150px; top: 92px; width: 300px;
  }
  .front-brand__name {
    font-weight: 700; font-size: 27px; line-height: 1.15;
    color: var(--logo-grey); letter-spacing: .5px;
  }
  .front-brand__mark {
    display: inline-block; width: 14px; height: 14px; border-radius: 50%;
    background: var(--brand-red); margin-bottom: 10px;
  }
  .front-brand__cities {
    margin-top: 8px; font-size: 14px; color: var(--brand-red);
  }
  .front-rule {
    position: absolute; left: 0; top: 262px; width: 360px; height: 2px;
    background: var(--brand-red);
  }
  .front-web {
    position: absolute; right: 34px; top: 246px;
    font-size: 12px; color: var(--brand-red);
  }

  /* back */
  .back-brand {
    position: absolute; left: 250px; top: 42px;
    display: flex; align-items: center; gap: 8px;
    font-weight: 700; font-size: 17px; color: var(--ink);
  }
  .back-brand__mark {
    width: 12px; height: 12px; background: var(--brand-red);
  }
  .back-divider { position: absolute; left: 0; top: 96px; }
  .contact-name {
    position: absolute; left: 30px; top: 122px;
    font-size: 26px; font-weight: 600; color: var(--ink-soft);
  }
  .contact-title {
    position: absolute; left: 30px; top: 156px;
    font-size: 20px; color: var(--brand-red);
  }
  .contact-list {
    position: absolute; left: 30px; top: 206px; list-style: none;
    font-size: 13px; color: var(--ink-soft);
  }
  .contact-list li {
    display: flex; align-items: center; gap: 10px; height: 26px;
  }
  .contact-list svg { flex: none; }
  .back-web {
    position: absolute; right: 26px; top: 262px;
    font-size: 12px; color: var(--brand-red);
  }
  .back-rule {
    position: absolute; left: 150px; top: 292px; width: 300px; height: 2px;
    background: var(--brand-red);
  }
</style>
</head>
<body>
<main class="canvas">

  <section class="card card--front" aria-label="Card front">
    <div class="front-brand">
      <span class="front-brand__mark" aria-hidden="true"></span>
      <p class="front-brand__name">Harbourline Supply Pty Ltd</p>
      <p class="front-brand__cities">Adelaide, Brisbane and Darwin</p>
    </div>
    <span class="front-web">www.harbourlinesupply.com.au</span>
    <div class="front-rule"></div>
  </section>

  <section class="card card--back" aria-label="Card back">
    <div class="back-brand">
      <span class="back-brand__mark" aria-hidden="true"></span>
      <span>Harbourline Supply Pty Ltd</span>
    </div>

    <svg class="back-divider" width="520" height="14" viewBox="0 0 520 14" aria-hidden="true">
      <path d="M0 4 H70 L80 10 H520" fill="none" stroke="var(--brand-red)" stroke-width="2"/>
      <rect x="0" y="4" width="72" height="8" fill="var(--brand-red)"/>
    </svg>

    <h1 class="contact-name">Vernon Ashcombe</h1>
    <p class="contact-title">General Manager</p>

    <ul class="contact-list">
      <li>
        <svg width="12" height="14" viewBox="0 0 12 14" aria-hidden="true">
          <rect x="1" y="1" width="10" height="12" rx="2" fill="none" stroke="var(--brand-red)" stroke-width="1.5"/>
        </svg>
        0427 619 354
      </li>
      <li>
        <svg width="14" height="10" viewBox="0 0 14 10" aria-hidden="true">
          <rect x="0" y="0" width="14" height="10" rx="1" fill="var(--brand-red)"/>
          <path d="M0 0 L7 6 L14 0" fill="none" stroke="#fff" stroke-width="1"/>
        </svg>
        vern@harbourlinesupply.com.au | vern@coastwardgoods.com.au
      </li>
    </ul>

    <span class="back-web">www.harbourlinesupply.com.au</span>
    <div class="back-rule"></div>
  </section>

</main>
</body>
</html>
```